Medical marijuana farm

I need a professional looking letterhead for my incorporated company

TERRA-BLOOM Inc.

"Copper Ridge Farm"

I want the name "Terra bloom" done in a lime green colour, with a black background.... Also- instead of a hyphen I would like a creative "+" sign....

4817 alder street, Nova Scotia is the civic address

902-555-0183

```html
<!DOCTYPE html>
<html lang="en">
<head>
<meta charset="utf-8">
<title>Terra Bloom Letterhead</title>
<link rel="stylesheet" href="https://fonts.googleapis.com/css2?family=Oswald:wght@500&family=Open+Sans:wght@700&family=PT+Sans+Narrow:wght@700&display=swap">
<style>
  :root {
    --page: #ffffff;
    --ink: #000000;
    --lime: #5cb849;
    --lime-line: #4fae3f;
    --lime-deep: #2f6e25;
  }
  html, body {
    margin: 0;
    padding: 0;
    overflow: hidden;
    background: var(--page);
  }
  .letterhead {
    position: relative;
    width: 1200px;
    height: 392px;
    overflow: hidden;
    background: var(--page);
  }
  .letterhead__banner {
    position: absolute;
    inset: 0;
    width: 1200px;
    height: 392px;
  }
  .banner__fill { fill: var(--ink); }
  .banner__frame {
    fill: none;
    stroke: var(--lime-line);
    stroke-width: 2.4;
    stroke-linejoin: miter;
  }
  .emblem-area {
    position: absolute;
    left: 60px;
    top: 50px;
    width: 235px;
    height: 272px;
    border-radius: 50%;
    background: radial-gradient(ellipse at center, var(--lime) 0%, var(--lime-deep) 55%, rgba(0,0,0,0) 72%);
  }
  .brand {
    position: absolute;
    right: 14px;
    top: 20px;
    margin: 0;
    font-family: "Oswald", "Arial Narrow", sans-serif;
    font-weight: 500;
    font-size: 78px;
    line-height: 1;
    letter-spacing: 4px;
    color: var(--lime);
    white-space: nowrap;
  }
  .farm-name {
    position: absolute;
    left: 690px;
    top: 134px;
    margin: 0;
    font-family: "Open Sans", "Verdana", sans-serif;
    font-weight: 700;
    font-size: 31px;
    line-height: 1;
    letter-spacing: 1px;
    color: var(--ink);
    -webkit-text-stroke: 1.6px var(--lime);
    white-space: nowrap;
  }
  .contact {
    position: absolute;
    left: 690px;
    top: 186px;
    margin: 0;
    padding: 0;
    list-style: none;
    font-family: "PT Sans Narrow", "Arial Narrow", sans-serif;
    font-weight: 700;
    font-size: 19px;
    line-height: 23.5px;
    color: var(--lime);
    white-space: nowrap;
  }
</style>
</head>
<body>
  <main class="letterhead">
    <svg class="letterhead__banner" viewBox="0 0 612 200" preserveAspectRatio="none" aria-hidden="true">
      <path class="banner__fill" d="M0 0 H612 V156 L540 180 L480 170 L400 194 L320 170 L240 194 L155 170 L100 194 L0 166 Z"/>
      <path class="banner__frame" d="M7 4 H605 V150 L540 172 L480 162 L400 186 L320 162 L240 186 L155 162 L100 186 L7 158 Z"/>
    </svg>

    <div class="emblem-area" role="img" aria-label="Green leaf emblem artwork"></div>

    <h1 class="brand">TERRA+BLOOM</h1>
    <p class="farm-name">Copper Ridge Farm</p>
    <ul class="contact">
      <li>Phone # 902-555-0183</li>
      <li>Fax #</li>
      <li>E-Mail Address</li>
      <li>4817 Alder Street, Nova Scotia</li>
    </ul>
  </main>
</body>
</html>
```